PLUME Residence One-Page Inserts

We need TWO one-page insert for a transplant display stand (6"x8"). We have a few furnished apartments and we need to inform our guests about the services available:

Insert #1: Delivery and Pickup Services in the neighborhood (Laundry, Groceries, Restaurants).
Insert #1 Text: "Heading: Pick and Delivery Services in your neighborhood:" Text below it: "1) Laundry Pickup - Call: +9714-382-7160. 2) Groceries Delivery - Call: +9714-382-7160, 3) Restaurants Delivery - Call: +9714-382-7160"

Insert #2: We also need another one-page insert to encourage the guests to enjoy the candles and to make the apartment have a homier feeling.
Insert #2 Text: "Heading: Feel at home. Text below it: "Dim the lights, light up a candle, play nice music, have a relaxing stay."

Target Market(s)

Staybrook Users. Apartment Guests. Tourist. Age Group 20 to 60 years old.

Industry/Entity Type

Hotel

Requirements
Must have
• - The Company logo of PLUME Residence must be displayed on the upper corner. (Logo attached). The logo should be a single color either white or black (Not red and black or red and white)
• For Insert # 1: Laundry, Groceries, and Breakfast Resturaunts images or icons. The images/icons must be unified and look like from the same family of images/icons.
• For Insert # 2: A romantic candle(s) dinner pictures.
Nice to have
• Not too many colors
• Not too busy
• Simple
• Eye Catchy
Should not have
• Lots of colors
• Too many images
• Too Busy

```html
<!DOCTYPE html>
<html lang="en">
<head>
<meta charset="utf-8">
<title>PLUME Residence – Feel at home</title>
<link rel="stylesheet" href="https://fonts.googleapis.com/css2?family=Questrial&family=Arimo:wght@400&display=swap">
<style>
  :root {
    --paper: #ffffff;
    --ink: #1f1f1f;
    --sage: #7f9c7f;
    --light-text: #ffffff;
    --photo-deep: #1b1712;
    --photo-mid: #4a3f33;
    --photo-warm: #8a7158;
  }
  * { margin: 0; padding: 0; box-sizing: border-box; }
  html, body {
    width: 936px;
    height: 1200px;
    overflow: hidden;
    background: var(--paper);
  }
  .insert {
    position: relative;
    width: 936px;
    height: 1200px;
    background: var(--paper);
    font-family: "Arimo", Arial, sans-serif;
  }
  .brand-bar {
    height: 152px;
    display: flex;
    align-items: center;
    justify-content: center;
  }
  .brand-name {
    font-family: "Questrial", sans-serif;
    font-size: 78px;
    letter-spacing: 4px;
    color: var(--ink);
    line-height: 1;
    margin-top: 18px;
  }
  .dinner-photo {
    height: 407px;
    background:
      radial-gradient(ellipse at 50% 30%, var(--photo-warm) 0%, transparent 45%),
      radial-gradient(ellipse at 50% 80%, var(--photo-mid) 0%, transparent 70%),
      linear-gradient(180deg, var(--photo-mid) 0%, var(--photo-deep) 100%);
  }
  .message-panel {
    height: 641px;
    background: var(--sage);
    text-align: center;
    position: relative;
  }
  .headline {
    font-family: "Questrial", sans-serif;
    font-weight: 400;
    font-size: 62px;
    word-spacing: 12px;
    color: var(--light-text);
    padding-top: 72px;
    line-height: 1;
  }
  .invitation {
    margin-top: 58px;
    font-size: 33px;
    line-height: 45px;
    color: var(--ink);
  }
  .website {
    position: absolute;
    left: 0;
    right: 0;
    bottom: 52px;
    font-size: 20px;
    color: var(--light-text);
    letter-spacing: 0.3px;
  }
</style>
</head>
<body>
  <main class="insert">
    <header class="brand-bar">
      <div class="brand-name">PLUME</div>
    </header>
    <div class="dinner-photo" role="img" aria-label="Candlelit dinner table set for two with wine glasses, oysters and plated meals"></div>
    <section class="message-panel">
      <h1 class="headline">Feel at home</h1>
      <p class="invitation">
        Dim the lights,<br>
        light up a candle,<br>
        play nice music,<br>
        have a relaxing stay.
      </p>
      <p class="website">www.plumeresidence.com</p>
    </section>
  </main>
</body>
</html>
```